Homepage mockup for PivotScoreHub.com

I would like a homepage mockup of pivotscorehub.com.

Basically what the site does, is it allows a person to upload a video of a gymnastics routine and our certified judges will judge the routine providing a score, as well as provide a critique and feedback as to why they gave you that score. Many times people don't know why they got the score they did at a gymnastics competition, so this site aims to provide reasoning behind it.

I have started to design the homepage myself (see attached), and like it, but I'd like a professional to finish the layout, or even come up with something really wow and original. I like clean, typically simple design.

THIS IS AN OLD VERSION OF THE SITE (http://esite.kralvenot.com/) This should only be used so you can get an idea of what the site is about. I DO NOT want the new site to look like this, but the basic concept and content remains the same.

DESIGNER FILES CAN BE DOWNLOADED HERE (http://kralvenot.com/files.aspx)

Target Market(s)

Gymnastic type people, parents of gymnasts, coaches, etc.

Industry/Entity Type

It Professional

Requirements
Must have
• -Pivot score hub logo (provided)
-Not required, but I have attached the main photo I used in my mockup (AI File)
*A step by step graphic(s) depicting the process for a user. A How it works sort of explanation. Should be eye catching, not just text.

-Step 1: Videotape your gymnastic routine.
-Step 2: Create an account and share us your video.
-Step 3: Our certified judges will score and critique your routine, fully explaining the reasons behind their score.

```html
<!DOCTYPE html>
<html lang="en">
<head>
<meta charset="utf-8">
<title>Pivot Score Hub — Get Judged Now</title>
<link rel="stylesheet" href="https://fonts.googleapis.com/css2?family=Ubuntu:wght@400;500;700&family=Arimo:wght@400;700&family=Nothing+You+Could+Do&display=swap">
<style>
  :root {
    --brand-blue: #3a78b0;
    --step-blue: #3a7db8;
    --heading-red: #c0343c;
    --cta-red: #a81010;
    --nav-red: #d8353d;
    --nav-red-dark: #b3222a;
    --text-grey: #555;
    --muted: #9a9a9a;
    --light: #c8c8c8;
    --panel: #f3f3f3;
    --footer: #333333;
    --arrow-green: #3aa53a;
    --signin-blue: #4a6f96;
  }
  * { box-sizing: border-box; margin: 0; padding: 0; }
  html, body { width: 1200px; height: 885px; overflow: hidden; }
  body { position: relative; background: #fff; font-family: "Ubuntu", sans-serif; color: var(--text-grey); }

  .site-header { position: absolute; left: 0; top: 0; width: 1200px; height: 126px; background: linear-gradient(#fafafa, #e4e4e4); }
  .brand { position: absolute; left: 136px; top: 28px; display: flex; align-items: center; gap: 10px; }
  .brand-mark { width: 14px; height: 14px; border-radius: 50%; background: var(--brand-blue); }
  .brand-name { font-family: "Ubuntu", sans-serif; font-weight: 500; font-size: 30px; color: var(--brand-blue); line-height: 1.1; width: 190px; }

  .main-nav { position: absolute; left: 470px; top: 38px; width: 592px; height: 50px; background: linear-gradient(var(--nav-red), var(--nav-red-dark)); transform: skewX(-4deg); border-radius: 3px; box-shadow: 0 3px 4px rgba(0,0,0,.25); border: 2px solid #fff; }
  .main-nav ul { list-style: none; display: flex; transform: skewX(4deg); height: 100%; align-items: center; padding-left: 42px; gap: 0; }
  .main-nav a { color: #fff; text-decoration: none; font-family: "Arimo", sans-serif; font-size: 16px; margin-right: 40px; }

  .hero { position: absolute; left: 0; top: 126px; width: 1200px; height: 364px; background: #fff; box-shadow: 0 3px 5px rgba(0,0,0,.12); }
  .hero-title { position: absolute; left: 137px; top: 28px; font-size: 34px; font-weight: 400; color: var(--heading-red); line-height: 31px; }
  .hero-intro { position: absolute; left: 138px; top: 102px; width: 465px; font-size: 12px; line-height: 15px; color: var(--light); }
  .process-list { position: absolute; left: 130px; top: 160px; list-style: none; }
  .process-list li { position: relative; padding-left: 53px; height: 46px; }
  .process-list .num { position: absolute; left: 0; top: 1px; width: 41px; height: 41px; border-radius: 50%; background: var(--step-blue); color: #fff; font-size: 18px; font-weight: 700; display: flex; align-items: center; justify-content: center; }
  .process-list h3 { font-size: 19px; font-weight: 400; color: #2e5f86; line-height: 22px; }
  .process-list p { font-size: 11px; color: #aaa; line-height: 13px; width: 210px; }
  .cta-heading { position: absolute; left: 418px; top: 172px; width: 182px; text-align: center; font-size: 33px; font-weight: 700; color: var(--cta-red); line-height: 36px; letter-spacing: -.5px; }
  .cta-why { position: absolute; left: 582px; top: 224px; font-family: "Nothing You Could Do", cursive; color: #4a9ad8; font-size: 18px; transform: rotate(-10deg); }
  .cta-button { position: absolute; left: 412px; top: 273px; width: 206px; height: 52px; border-radius: 12px; background: #e8e8e8; border: 1px solid #ccc; padding: 5px; }
  .cta-button span { display: flex; align-items: center; height: 100%; border-radius: 9px; background: linear-gradient(#2a55c8, #1a3596); color: #fff; padding: 0 8px; gap: 10px; }
  .cta-button small { font-family: "Arimo", sans-serif; font-size: 10px; line-height: 11px; text-align: center; }
  .cta-button b { font-family: "Arimo", sans-serif; font-size: 16px; }

  .hero-banner { position: absolute; left: 638px; top: 100px; width: 407px; height: 448px; }
  .hero-banner .tab { position: absolute; top: 2px; width: 20px; height: 26px; background: #333; border-radius: 10px 10px 0 0; }

  .steps { position: absolute; left: 111px; top: 553px; }
  .step-card { position: absolute; top: 15px; height: 225px; background: linear-gradient(#f0f0f0, #f9f9f9); border: 1px solid #e0e0e0; border-radius: 3px; text-align: center; }
  .step-card h4 { position: absolute; left: 18px; top: 24px; text-align: left; font-size: 17px; font-weight: 400; color: var(--step-blue); line-height: 18px; }
  .step-card .icon { position: absolute; left: 50%; top: 78px; width: 120px; height: 72px; transform: translateX(-50%); border-radius: 6px; }
  .step-card p { position: absolute; left: 8px; right: 8px; top: 180px; font-size: 13.5px; color: #444; line-height: 16px; }
  .step-badge { position: absolute; top: -14px; width: 44px; height: 44px; border-radius: 50%; background: radial-gradient(circle at 40% 35%, #d6262a, #9e0c10); border: 2px solid #fff; color: #fff; font-weight: 700; font-size: 18px; display: flex; align-items: center; justify-content: center; box-shadow: 0 1px 3px rgba(0,0,0,.3); }
  .step-arrow { position: absolute; top: 124px; }

  .sign-in { position: absolute; left: 790px; top: 573px; width: 297px; height: 218px; background: #fff; border: 1px solid #d6d6d6; border-radius: 3px; box-shadow: 0 1px 3px rgba(0,0,0,.1); }
  .sign-in header { height: 54px; background: linear-gradient(#f8f8f8, #ececec); display: flex; justify-content: space-between; align-items: center; padding: 0 18px; }
  .sign-in h2 { font-size: 19px; font-weight: 500; color: #333; }
  .sign-in header span { font-size: 11.5px; color: #666; }
  .sign-in header b { color: #333; }
  .field { position: absolute; left: -5px; width: 306px; height: 32px; background: linear-gradient(#f7f7f7, #e6e6e6); border: 1px solid #ddd; display: flex; align-items: center; }
  .field label { width: 80px; height: 32px; background: #b8262c; color: #fff; font-family: "Arimo", sans-serif; font-weight: 700; font-size: 10px; display: flex; align-items: center; padding-left: 10px; clip-path: polygon(0 0, 88% 0, 100% 50%, 88% 100%, 0 100%); }
  .field span { margin-left: 14px; font-family: "Arimo", sans-serif; font-size: 13px; color: #777; }
  .remember { position: absolute; left: 20px; top: 148px; display: flex; align-items: center; gap: 5px; font-size: 12px; color: #666; }
  .remember i { width: 12px; height: 12px; border: 1px solid #4a6f96; display: inline-flex; align-items: center; justify-content: center; }
  .forgot { position: absolute; right: 20px; top: 148px; font-size: 12px; color: #666; }
  .sign-in-button { position: absolute; left: 0; right: 0; bottom: 0; height: 36px; background: repeating-linear-gradient(135deg, #5a80a8 0 12px, #4a6f96 12px 24px); color: #fff; font-size: 19px; font-weight: 500; display: flex; align-items: center; justify-content: center; }

  .site-footer { position: absolute; left: 0; top: 827px; width: 1200px; height: 58px; background: var(--footer); color: #fff; font-size: 13.5px; font-weight: 500; }
  .site-footer .copy { position: absolute; left: 126px; top: 20px; }
  .site-footer nav { position: absolute; right: 117px; top: 19px; font-size: 14.5px; }
  .site-footer nav span { margin: 0 6px; }
</style>
</head>
<body>
  <header class="site-header">
    <div class="brand"><span class="brand-mark"></span><span class="brand-name">Pivot Score Hub</span></div>
    <nav class="main-nav"><ul>
      <li><a href="#">Home</a></li><li><a href="#">FAQ</a></li><li><a href="#">Sample</a></li>
      <li><a href="#">Critique</a></li><li><a href="#">Members Area</a></li><li><a href="#">About</a></li>
    </ul></nav>
  </header>

  <section class="hero">
    <h1 class="hero-title">Being Judged has never<br>been Easier</h1>
    <p class="hero-intro">Lorem ipsum dolor sit amet, consectetuer adipiscing elit, sed diam nonummy nibh euismod tincidunt ut laoreet dolore magna aliquam erat volutpat. Ut wisi enim ad minim veniam.</p>
    <ol class="process-list">
      <li><span class="num">1</span><h3>Record your routeen</h3><p>Videotape your gymnastic routine.</p></li>
      <li><span class="num">2</span><h3>Sign Up &amp; Upload</h3><p>Create an account and share us your video.</p></li>
      <li><span class="num">3</span><h3>Get the Why</h3><p>Our certified judges will score and critique your routine, fully explaining the reasons behind their score.</p></li>
    </ol>
    <div class="cta-heading">Get Judged Now !</div>
    <div class="cta-why">Why</div>
    <a class="cta-button"><span><small>Upload your video<br>&amp; get critiqued!</small><b>Get started</b></span></a>
  </section>

  <div class="hero-banner">
    <span class="tab" style="left:-18px"></span><span class="tab" style="right:-18px"></span>
    <svg width="407" height="448" viewBox="0 0 407 448" role="img" aria-label="Gymnast in a mid-air split leap with glowing light trails, and score cards reading 8, 7.5 and 6.5">
      <defs>
        <radialGradient id="bannerFill" cx="50%" cy="45%" r="65%">
          <stop offset="0" stop-color="#f6d8cc"/><stop offset=".5" stop-color="#f4ece6"/><stop offset="1" stop-color="#f2f2f2"/>
        </radialGradient>
      </defs>
      <path d="M0 0H407V420L203 448L0 420Z" fill="url(#bannerFill)" stroke="#e2e2e2"/>
    </svg>
  </div>

  <section class="steps">
    <article class="step-card" style="left:0;width:215px">
      <h4>Upload Your Video</h4>
      <div class="icon" role="img" aria-label="Folder with download arrow" style="background:linear-gradient(#8a8a8a,#4a4a4a)"></div>
      <p>Videotape your gymnastic routine</p>
    </article>
    <span class="step-badge" style="left:178px">1</span>
    <svg class="step-arrow" style="left:203px" width="42" height="26" viewBox="0 0 42 26"><path d="M0 8H24V0L42 13L24 26V18H0Z" fill="var(--arrow-green)"/></svg>

    <article class="step-card" style="left:229px;width:211px">
      <h4>We'll judge your routine</h4>
      <div class="icon" role="img" aria-label="Group of judges" style="background:linear-gradient(#e0a070,#c8703a)"></div>
      <p>Create an account and share us your video.</p>
    </article>
    <span class="step-badge" style="left:401px">2</span>
    <svg class="step-arrow" style="left:425px" width="42" height="26" viewBox="0 0 42 26"><path d="M0 8H24V0L42 13L24 26V18H0Z" fill="var(--arrow-green)"/></svg>

    <article class="step-card" style="left:452px;width:211px">
      <h4>Get the “why” &amp; much,<br>much  more!</h4>
      <div class="icon" role="img" aria-label="Thumbs up hand" style="background:linear-gradient(#f0c8a0,#3a5a90)"></div>
      <p>Our certified judges will score and critique your routine</p>
    </article>
    <span class="step-badge" style="left:624px">3</span>
  </section>

  <form class="sign-in">
    <header><h2>Sign In</h2><span>join us now <b>for free!</b></span></header>
    <div class="field" style="top:55px"><label>USERNAME</label><span>Dana Whitlock</span></div>
    <div class="field" style="top:97px"><label>PASSWORD</label><span>**********</span></div>
    <div class="remember"><i><svg width="10" height="10" viewBox="0 0 10 10"><path d="M1 5L4 8L9 1" stroke="#2a4f86" stroke-width="2" fill="none"/></svg></i>remember me</div>
    <div class="forgot">forgot your Login?</div>
    <div class="sign-in-button">Sign in</div>
  </form>

  <footer class="site-footer">
    <div class="copy">Copyright 2010 , Pivot Score Hub. All rights reserved.</div>
    <nav>Home<span>|</span>FAQ<span>|</span>Sample<span>|</span>Critique<span>|</span>Members Area<span>|</span>About</nav>
  </footer>
</body>
</html>
```